Orbit 582 - Kindle Book Cover

I am looking for a Kindle book cover for my book about "Orbit 582".
The Book is Titled:
Orbit 582 Ascended
Shaping Tomorrow: Paths To Unlocking Hidden Currents
Author is Dorian Welby
Here is a book description that may help you understand more about it:
Inspired by the genius of Bertram Ollinger, this comprehensive guide delves into the ancient wisdom and cutting-edge science behind the 582 method, a powerful tool for manifesting your desires. Whether you're seeking personal growth, financial success, or spiritual enlightenment, this book provides advanced techniques and methods to transform your dreams into reality.
Any questions please ask.
Thanks
Gavin

```html
<!DOCTYPE html>
<html lang="en">
<head>
<meta charset="utf-8">
<title>Orbit 582 Ascended — Dorian Welby</title>
<link rel="stylesheet" href="https://fonts.googleapis.com/css2?family=Cinzel:wght@400;500&family=Cormorant+Garamond:wght@400;500&display=swap">
<style>
  :root {
    --backdrop: #d3d3d3;
    --gold: #f2c58a;
    --sky-deep: #2a1c40;
    --sky-violet: #4a2350;
    --glow-core: #f4d6b0;
    --glow-amber: #c8704a;
    --ridge-rose: #8a3a4c;
    --sea-teal: #2f6f80;
    --floor-plum: #3a1f3e;
    --shadow: rgba(0, 0, 0, 0.28);
  }
  html, body {
    margin: 0;
    padding: 0;
    width: 1200px;
    height: 1200px;
    overflow: hidden;
    background: var(--backdrop);
  }
  .canvas {
    position: relative;
    width: 1200px;
    height: 1200px;
  }
  .cover {
    position: absolute;
    left: 258px;
    top: 54px;
    width: 684px;
    height: 1092px;
    overflow: hidden;
    box-shadow: 2px 3px 4px var(--shadow);
  }
  .cover-art {
    position: absolute;
    inset: 0;
    background:
      radial-gradient(ellipse 18% 12% at 50% 44%, var(--glow-core) 0%, rgba(244,214,176,0) 100%),
      radial-gradient(ellipse 40% 34% at 50% 44%, rgba(200,112,74,0.8) 0%, rgba(200,112,74,0) 100%),
      radial-gradient(ellipse 40% 22% at 15% 10%, rgba(47,111,128,0.7) 0%, rgba(47,111,128,0) 100%),
      radial-gradient(ellipse 30% 18% at 85% 15%, rgba(60,80,150,0.6) 0%, rgba(60,80,150,0) 100%),
      radial-gradient(ellipse 60% 14% at 50% 68%, rgba(47,111,128,0.6) 0%, rgba(47,111,128,0) 100%),
      radial-gradient(ellipse 70% 25% at 50% 56%, rgba(138,58,76,0.8) 0%, rgba(138,58,76,0) 100%),
      radial-gradient(ellipse 40% 20% at 50% 82%, rgba(160,70,90,0.6) 0%, rgba(160,70,90,0) 100%),
      linear-gradient(180deg, var(--sky-deep) 0%, var(--sky-violet) 30%, var(--ridge-rose) 55%, var(--floor-plum) 80%, var(--sky-deep) 100%);
  }
  .cover-text {
    position: absolute;
    inset: 0;
    color: var(--gold);
    text-align: center;
  }
  .subtitle {
    position: absolute;
    top: 123px;
    left: 0;
    right: 0;
    margin: 0;
    font-family: "Cormorant Garamond", serif;
    font-weight: 500;
    font-size: 17px;
    line-height: 26px;
    letter-spacing: 0.3px;
    text-transform: uppercase;
  }
  .title {
    margin: 0;
    font-weight: 400;
  }
  .title-word {
    position: absolute;
    top: 304px;
    left: 0;
    right: 0;
    font-family: "Cinzel", serif;
    font-size: 84px;
    line-height: 1;
    letter-spacing: 12px;
    padding-left: 12px;
  }
  .title-number {
    position: absolute;
    top: 377px;
    left: 0;
    right: 0;
    font-family: "Cinzel", serif;
    font-size: 165px;
    line-height: 1;
    letter-spacing: 2px;
  }
  .title-edition {
    position: absolute;
    top: 560px;
    left: 0;
    right: 0;
    font-family: "Cinzel", serif;
    font-size: 22px;
    line-height: 1;
    letter-spacing: 8px;
    padding-left: 8px;
  }
  .author {
    position: absolute;
    top: 941px;
    left: 0;
    right: 0;
    margin: 0;
    font-family: "Cinzel", serif;
    font-weight: 400;
    font-size: 45px;
    line-height: 1;
    letter-spacing: 3px;
  }
</style>
</head>
<body>
<main class="canvas">
  <article class="cover">
    <div class="cover-art" role="img" aria-label="Surreal landscape: glowing nebula sky over pink and teal mountains, a lone figure standing on a reflective shore"></div>
    <div class="cover-text">
      <p class="subtitle">Shaping Tomorrow<br>Paths To Unlocking Hidden Currents</p>
      <h1 class="title">
        <span class="title-word">ORBIT</span>
        <span class="title-number">582</span>
        <span class="title-edition">ASCENDED</span>
      </h1>
      <p class="author">DORIAN WELBY</p>
    </div>
  </article>
</main>
</body>
</html>
```